Startup Jewelry Needs a fully coded Ecommerce Website

Description

We want the full coded woocommerce website - website to be operational and fully integrated with Tendrix and other gateways .
We sell jewelry items like rings,ear rings,chain, necklaces etc.

Color Preference
Colors to be used are Velvet red, Black / anthracite, exclusive colors, silver-white, bronze-brown and golden.

Functionalities
Regarding Functions, the store will have functions of typical ecommerce jewelry store using the products/categories for the starting page, going into individual product pages by clicking these images and then leading to a detailed page for one product only.

Target Market
Jewelry-lovers, who appreciate extraordinary things, creative economy/fashion-industries, stylists, Style consultants, outfitter, theaters, operas, production sites, Cocktail-, Dinner and Bride-fashion etc

Look and Feel
Each slider illustrates characteristics of the customer's brand and the style your web design should communicate.

Must have
Logo must be designed

Should Not Have:
- - Dull and common design
- - Messy/unstructured navigation

Industry/Entity Type

Jewelry

Coding

Coded - Design and coding required

```html
<!DOCTYPE html>
<html lang="en">
<head>
<meta charset="utf-8">
<title>Aurelle Jewels — Store</title>
<link href="https://fonts.googleapis.com/css2?family=Open+Sans:wght@400;600;700&family=Oswald:wght@400;500&display=swap" rel="stylesheet">
<style>
:root{
  --velvet:#8e1b2e;
  --velvet-dark:#6e1222;
  --gold:#c9a24a;
  --gold-bright:#e0b84f;
  --bronze:#8a5a32;
  --anthracite:#2a2a2c;
  --silver:#e8e8ea;
  --ink:#222;
  --line:#d9d9d9;
  --panel:#ececee;
  --sale:#b3263a;
  --white:#fff;
}
*{margin:0;padding:0;box-sizing:border-box}
html,body{width:1200px;height:2467px;overflow:hidden;background:var(--white)}
body{position:relative;font-family:"Open Sans",Arial,sans-serif;color:var(--ink)}
a{color:inherit;text-decoration:none}
.abs{position:absolute}

/* top bar */
.topbar{left:0;top:0;width:1200px;height:54px;background:var(--anthracite);color:var(--silver);font-size:12px;display:flex;align-items:center;padding:0 50px;border-bottom:3px solid var(--velvet)}
.topbar .cart{display:flex;align-items:center;gap:10px}
.topbar .account-links{margin-left:auto;display:flex;gap:34px}
.topbar .account-links span{display:flex;align-items:center;gap:8px}

/* header */
.header{left:0;top:54px;width:1200px;height:173px;background:linear-gradient(#fff,#ececee)}
.brand{display:flex;align-items:center;gap:12px}
.brand .mark{width:34px;height:34px;border-radius:50%;background:var(--gold)}
.brand .name{font-weight:600;color:var(--velvet);font-size:22px}
.header .brand{position:absolute;left:50px;top:66px}
.search{position:absolute;left:388px;top:59px;width:424px;height:52px;background:var(--white);border:1px solid #cfcfcf;display:flex;align-items:center;padding:0 18px;font-size:11px;color:#777}
.search svg{margin-left:auto}
.contact-info{position:absolute;left:991px;top:56px;font-size:11px;color:#333}
.contact-info div{display:flex;align-items:center;gap:12px;height:30px}

/* nav */
.mainnav{left:0;top:227px;width:1200px;height:67px;background:var(--white);display:flex;align-items:center;padding-left:50px;border-bottom:1px solid #eee}
.mainnav a{color:var(--velvet);font-size:16px;margin-right:37px}

/* hero */
.hero{left:0;top:294px;width:1200px;height:366px;background:radial-gradient(ellipse 420px 260px at 78% 40%,#1c1416 0%,#070707 70%),#050505;overflow:hidden}
.hero .photo{position:absolute;left:0;top:0;width:660px;height:366px;
  background:
    radial-gradient(ellipse 130px 150px at 330px 120px,#c9c9cc 0%,#8d8d90 45%,rgba(20,20,20,0) 100%),
    radial-gradient(ellipse 230px 60px at 330px 330px,#e6e6e8 0%,#9a9a9e 40%,rgba(10,10,10,0) 100%),
    linear-gradient(90deg,#0a0a0a 0%,#2c2c2e 30%,#3a3a3c 55%,#050505 100%)}
.hero .offer{position:absolute;left:855px;top:22px;color:var(--gold-bright);font-size:38px;font-weight:400}
.hero .title{position:absolute;left:843px;top:64px;color:var(--gold-bright);font-family:"Oswald",sans-serif;font-size:56px;letter-spacing:9px;font-weight:500}
.hero .btn{position:absolute;left:681px;top:242px;width:131px;height:39px;background:var(--white);border:2px solid var(--velvet);color:var(--velvet);font-size:15px;display:flex;align-items:center;justify-content:center}

/* sidebar */
.sidebar{left:49px;top:708px;width:360px;height:1122px;border:1px solid var(--line);padding:0 14px}
.sidebar h3{font-size:15px;font-weight:400;color:#222;padding-bottom:6px;border-bottom:1px solid var(--line)}
.cat-list{list-style:none;font-size:11px;color:#333;margin-top:6px;padding-bottom:12px;border-bottom:1px solid var(--line)}
.cat-list li{line-height:16.5px}
.cat-list li::before{content:"»";color:#999;margin-right:6px}
.promo{position:relative;width:331px;height:237px}
.promo .badge{position:absolute;left:0;top:0;width:138px;height:37px;background:var(--velvet);color:var(--white);font-size:14px;font-weight:600;display:flex;align-items:center;justify-content:center}
.newsletter p{font-size:14px;color:#333;margin-top:14px}
.newsletter .field{width:250px;height:45px;background:var(--panel);margin-top:18px;border-radius:3px}
.newsletter .subscribe{width:133px;height:45px;background:var(--velvet);color:var(--white);font-weight:700;font-size:14px;border-radius:23px;display:flex;align-items:center;justify-content:center;margin-top:24px}
.social{display:flex;align-items:center;gap:8px;margin-top:28px;font-size:14px;color:#333}
.social .dot{width:9px;height:9px;border-radius:50%;background:var(--velvet)}

/* section bars */
.section-bar{height:37px;background:var(--velvet);color:var(--white);display:flex;align-items:center;padding-left:24px;font-size:15px;position:relative}
.section-bar .tabs{position:absolute;display:flex;align-items:center;font-size:15px;color:var(--silver)}
.section-bar .tabs .sep{margin:0 22px}
.section-bar .views{position:absolute;right:0;top:0;height:37px;display:flex;align-items:center;gap:12px;padding-right:4px}
.section-bar .views span{width:30px;height:30px;background:var(--white);display:flex;align-items:center;justify-content:center}

.grid{display:grid;grid-template-columns:repeat(3,190px);column-gap:69px;row-gap:32px;margin-top:30px}
.card .pic{width:190px;height:146px}
.card .title{font-size:14px;color:#444;margin-top:4px}
.card .price{font-size:14px;margin-top:5px;display:flex;align-items:center;gap:4px;white-space:nowrap}
.card .price s{color:var(--sale)}
.card .price b{font-weight:600}
.card .stars{color:var(--gold);font-size:15px;letter-spacing:1px;margin-left:2px}
.see-all{height:37px;background:var(--panel);display:flex;align-items:center;justify-content:center;font-size:15px;color:#333}

/* image fills */
.dark-gold{background:radial-gradient(circle at 50% 50%,#b8892c 0%,#3a2a10 35%,#050505 70%)}
.dark-silver{background:radial-gradient(ellipse at 50% 50%,#d9d9d9 0%,#6c6c6c 35%,#050505 70%)}
.dark-blue{background:radial-gradient(circle at 50% 60%,#7aa8d8 0%,#2a3a4a 30%,#050505 65%)}
.light-gold{background:radial-gradient(ellipse at 50% 50%,#e6b43a 0%,#f0d9a0 45%,#f8f4ea 75%)}
.light-red{background:radial-gradient(circle at 50% 50%,#c41e45 0%,#e0a940 35%,#f6efe0 75%)}
.light-heart{background:radial-gradient(circle at 50% 50%,#ddd 0%,#e7b33a 35%,#fbf7ee 70%)}

/* footer */
.footer{left:0;top:2165px;width:1200px;height:302px;background:var(--anthracite);color:#ddd;border-top:3px solid var(--velvet)}
.footer .brand{position:absolute;left:50px;top:28px}
.footer .brand .name{color:var(--gold-bright)}
.footer .about{position:absolute;left:50px;top:110px;width:280px;font-size:11px;line-height:14px;text-align:justify;color:#e6e6e6}
.footer .col{position:absolute;top:80px;font-size:11px;line-height:15px}
.footer .col h4{font-size:15px;font-weight:600;color:var(--white);margin-bottom:8px}
.footer .social-row{display:flex;gap:20px;margin-top:12px}
.footer .social-row span{width:11px;height:11px;border-radius:50%;background:var(--gold)}
.footer .copy{position:absolute;left:0;bottom:26px;width:1200px;text-align:center;font-size:15px;color:#ddd}
</style>
</head>
<body>

<div class="abs topbar">
  <div class="cart">
    <span>SHOPING CART</span>
    <svg width="18" height="16" viewBox="0 0 18 16"><path d="M1 1h3l2 9h9l2-7H5" fill="none" stroke="#e8e8ea" stroke-width="1.8"/><circle cx="7" cy="14" r="1.5" fill="#e8e8ea"/><circle cx="14" cy="14" r="1.5" fill="#e8e8ea"/></svg>
    <span>ITEMS : 20 &nbsp;$200</span>
  </div>
  <div class="account-links">
    <span><svg width="18" height="18" viewBox="0 0 18 18"><circle cx="9" cy="5" r="4" fill="#e8e8ea"/><path d="M1 18c0-5 4-8 8-8s8 3 8 8z" fill="#e8e8ea"/></svg>ACCOUNT</span>
    <span><svg width="26" height="18" viewBox="0 0 26 18"><rect x="0" y="2" width="15" height="11" fill="#e8e8ea"/><path d="M16 6h5l4 4v3h-9z" fill="#e8e8ea"/><circle cx="5" cy="15" r="2.5" fill="#e8e8ea"/><circle cx="20" cy="15" r="2.5" fill="#e8e8ea"/></svg>TRACK ORDER</span>
    <span><svg width="14" height="18" viewBox="0 0 14 18"><path d="M3 8V5a4 4 0 0 1 8 0v3" fill="none" stroke="#e8e8ea" stroke-width="2"/><rect x="0" y="8" width="14" height="10" fill="#e8e8ea"/></svg>LOGIN</span>
  </div>
</div>

<header class="abs header">
  <div class="brand"><span class="mark"></span><span class="name">Aurelle Jewels</span></div>
  <div class="search">Search Item Here
    <svg width="42" height="36" viewBox="0 0 42 36"><circle cx="15" cy="14" r="11" fill="none" stroke="#8e1b2e" stroke-width="4"/><path d="M23 22l14 11" stroke="#8e1b2e" stroke-width="5" stroke-linecap="round"/></svg>
  </div>
  <div class="contact-info">
    <div><svg width="20" height="20" viewBox="0 0 20 20"><rect width="20" height="20" rx="4" fill="#8e1b2e"/><path d="M6 4l3 3-2 2c1 2 2 3 4 4l2-2 3 3-2 2C9 16 4 11 4 6z" fill="#fff"/></svg>+44 0000 100200</div>
    <div><svg width="20" height="14" viewBox="0 0 20 14"><rect x="1" y="1" width="18" height="12" fill="none" stroke="#8e1b2e" stroke-width="1.5"/><path d="M1 1l9 7 9-7" fill="none" stroke="#8e1b2e" stroke-width="1.5"/></svg>username@example.com</div>
  </div>
</header>

<nav class="abs mainnav">
  <a>HOME</a><a>PRODUCTS</a><a>CATEGORY</a><a>GALLERY</a><a>ABOUT</a><a>CONTACT</a>
</nav>

<section class="abs hero">
  <div class="photo" role="img" aria-label="Black and white portrait of a model wearing a diamond necklace"></div>
  <div class="offer">25% OFF</div>
  <div class="title">NECKLACE</div>
  <a class="btn">VIEW ALL</a>
</section>

<aside class="abs sidebar">
  <h3 style="margin-top:14px">Categories</h3>
  <ul class="cat-list">
    <li>Earrings</li><li>Bracelets</li><li>Necklace</li><li>Rings</li><li>Watches</li><li>Wedding</li>
  </ul>
  <h3 style="margin-top:14px">Specials</h3>
  <div class="promo dark-gold" style="margin-top:10px" role="img" aria-label="Gold heart ring set with diamonds"><span class="badge">70% OFF</span></div>
  <div style="border-top:1px solid var(--line);margin-top:26px"></div>
  <h3 style="margin-top:18px">Deal Of The Day</h3>
  <div class="promo dark-gold" style="margin-top:6px" role="img" aria-label="Gold ring with a diamond cluster"><span class="badge">50% OFF</span></div>
  <div style="border-top:1px solid var(--line);margin-top:26px"></div>
  <div class="newsletter">
    <h3 style="margin-top:18px">NewsLetter Subscription</h3>
    <p>Sign Up for Our Newsletter!</p>
    <div class="field"></div>
    <a class="subscribe">SUBSCRIBE</a>
    <div class="social">Social Links : &nbsp;<span class="dot"></span><span class="dot"></span><span class="dot"></span><span class="dot"></span></div>
  </div>
</aside>

<main class="abs" style="left:444px;top:711px;width:711px">
  <div class="section-bar">LATEST ARIVALS
    <div class="tabs" style="left:255px">Rings<span class="sep">|</span>Bracelets<span class="sep">|</span>Earrings</div>
    <div class="views">
      <span><svg width="16" height="16" viewBox="0 0 16 16" fill="#8e1b2e"><rect width="7" height="7"/><rect x="9" width="7" height="7"/><rect y="9" width="7" height="7"/><rect x="9" y="9" width="7" height="7"/></svg></span>
      <span><svg width="18" height="16" viewBox="0 0 18 16" fill="#8e1b2e"><rect width="3" height="3"/><rect x="5" width="13" height="3"/><rect y="6.5" width="3" height="3"/><rect x="5" y="6.5" width="13" height="3"/><rect y="13" width="3" height="3"/><rect x="5" y="13" width="13" height="3"/></svg></span>
    </div>
  </div>
  <div class="grid">
    <div class="card"><div class="pic dark-gold" role="img" aria-label="Gold pendant earring with red stone"></div><div class="title">Lorem ipsum dolor</div><div class="price"><s>$10.00</s><b>$90.00</b><span class="stars">★★★★☆</span></div></div>
    <div class="card"><div class="pic dark-silver" role="img" aria-label="Thin gold and diamond bracelet"></div><div class="title">Lorem ipsum dolor</div><div class="price"><s>$10.00</s><b>$90.00</b><span class="stars">★★★★☆</span></div></div>
    <div class="card"><div class="pic dark-silver" role="img" aria-label="Silver ring with black stone"></div><div class="title">Lorem ipsum dolor</div><div class="price"><s>$10.00</s><b>$90.00</b><span class="stars">★★★★☆</span></div></div>
    <div class="card"><div class="pic dark-gold" role="img" aria-label="Gold flower ring with diamonds"></div><div class="title">Lorem ipsum dolor</div><div class="price"><s>$10.00</s><b>$90.00</b><span class="stars">★★★★☆</span></div></div>
    <div class="card"><div class="pic dark-blue" role="img" aria-label="Silver drop earrings with blue stones"></div><div class="title">Lorem ipsum dolor</div><div class="price"><s>$10.00</s><b>$90.00</b><span class="stars">★★★★☆</span></div></div>
    <div class="card"><div class="pic dark-silver" role="img" aria-label="Diamond tennis bracelet"></div><div class="title">Lorem ipsum dolor</div><div class="price"><s>$10.00</s><b>$90.00</b><span class="stars">★★★★☆</span></div></div>
  </div>
  <div class="see-all" style="margin-top:24px">SEE ALL</div>

  <div class="section-bar" style="margin-top:13px">FEATURED PRODUCTS
    <div class="tabs" style="left:255px">Rings<span class="sep">|</span>Bracelets<span class="sep">|</span>Earrings</div>
    <div class="views">
      <span><svg width="16" height="16" viewBox="0 0 16 16" fill="#8e1b2e"><rect width="7" height="7"/><rect x="9" width="7" height="7"/><rect y="9" width="7" height="7"/><rect x="9" y="9" width="7" height="7"/></svg></span>
      <span><svg width="18" height="16" viewBox="0 0 18 16" fill="#8e1b2e"><rect width="3" height="3"/><rect x="5" width="13" height="3"/><rect y="6.5" width="3" height="3"/><rect x="5" y="6.5" width="13" height="3"/><rect y="13" width="3" height="3"/><rect x="5" y="13" width="13" height="3"/></svg></span>
    </div>
  </div>
  <div class="grid" style="margin-top:31px">
    <div class="card"><div class="pic light-gold" role="img" aria-label="Engraved gold bangle"></div><div class="title">Lorem ipsum dolor</div><div class="price"><s>$10.00</s><b>$90.00</b><span class="stars">★★★★☆</span></div></div>
    <div class="card"><div class="pic light-heart" role="img" aria-label="Gold heart pendant with diamond stars"></div><div class="title">Lorem ipsum dolor</div><div class="price"><s>$10.00</s><b>$90.00</b><span class="stars">★★★★☆</span></div></div>
    <div class="card"><div class="pic dark-silver" role="img" aria-label="Diamond tennis bracelet"></div><div class="title">Lorem ipsum dolor</div><div class="price"><s>$10.00</s><b>$90.00</b><span class="stars">★★★★☆</span></div></div>
    <div class="card"><div class="pic dark-silver" role="img" aria-label="Wide diamond cluster bracelet"></div><div class="title">Lorem ipsum dolor</div><div class="price"><s>$10.00</s><b>$90.00</b><span class="stars">★★★★☆</span></div></div>
    <div class="card"><div class="pic light-red" role="img" aria-label="Gold mesh bracelet with ruby centre"></div><div class="title">Lorem ipsum dolor</div><div class="price"><s>$10.00</s><b>$90.00</b><span class="stars">★★★★☆</span></div></div>
    <div class="card"><div class="pic dark-silver" role="img" aria-label="Wide diamond cluster bracelet"></div><div class="title">Lorem ipsum dolor</div><div class="price"><s>$10.00</s><b>$90.00</b><span class="stars">★★★★☆</span></div></div>
  </div>
  <div class="see-all" style="margin-top:24px">SEE ALL</div>
</main>

<section class="abs" style="left:49px;top:1864px;width:1106px">
  <div class="section-bar">HOT DEALS
    <div class="tabs" style="left:225px">Rings<span class="sep">|</span>Bracelets<span class="sep">|</span>Earrings</div>
    <div class="views">
      <span><svg width="16" height="16" viewBox="0 0 16 16" fill="#8e1b2e"><rect width="7" height="7"/><rect x="9" width="7" height="7"/><rect y="9" width="7" height="7"/><rect x="9" y="9" width="7" height="7"/></svg></span>
      <span><svg width="18" height="16" viewBox="0 0 18 16" fill="#8e1b2e"><rect width="3" height="3"/><rect x="5" width="13" height="3"/><rect y="6.5" width="3" height="3"/><rect x="5" y="6.5" width="13" height="3"/><rect y="13" width="3" height="3"/><rect x="5" y="13" width="13" height="3"/></svg></span>
    </div>
  </div>
  <div style="display:grid;grid-template-columns:repeat(5,190px);column-gap:35px;margin:23px 0 0 5px">
    <div class="card"><div class="pic dark-silver" role="img" aria-label="Wide diamond cluster bracelet"></div><div class="title">Lorem ipsum dolor</div><div class="price"><s>$10.00</s><b>$90.00</b><span class="stars">★★★★☆</span></div></div>
    <div class="card"><div class="pic light-red" role="img" aria-label="Gold mesh bracelet with ruby centre"></div><div class="title">Lorem ipsum dolor</div><div class="price"><s>$10.00</s><b>$90.00</b><span class="stars">★★★★☆</span></div></div>
    <div class="card"><div class="pic dark-silver" role="img" aria-label="Wide diamond cluster bracelet"></div><div class="title">Lorem ipsum dolor</div><div class="price"><s>$10.00</s><b>$90.00</b><span class="stars">★★★★☆</span></div></div>
    <div class="card"><div class="pic light-gold" role="img" aria-label="Engraved gold bangle"></div><div class="title">Lorem ipsum dolor</div><div class="price"><s>$10.00</s><b>$90.00</b><span class="stars">★★★★☆</span></div></div>
    <div class="card"><div class="pic light-heart" role="img" aria-label="Gold heart pendant with diamond stars"></div><div class="title">Lorem ipsum dolor</div><div class="price"><s>$10.00</s><b>$90.00</b><span class="stars">★★★★☆</span></div></div>
  </div>
</section>

<footer class="abs footer">
  <div class="brand"><span class="mark"></span><span class="name">Aurelle Jewels</span></div>
  <p class="about">Lorem Ipsum is simply dummy text of the printing and typesetting industry.Lorem Ipsum is simply dummy text of the printing and typesetting industry.Lorem Ipsum is simply dummy text of the printing and typesetting industry.Lorem Ipsum is simply dummy text of the printing and typesetting industry.</p>
  <div class="col" style="left:437px"><h4>Company</h4>About Us<br>News &amp; Announcements<br>Testimonials</div>
  <div class="col" style="left:674px"><h4>Support</h4>FAQs<br>Terms of Service<br>Privacy Policy<br>Contact Us</div>
  <div class="col" style="left:891px"><h4>Contact</h4>+91 00 1234 5678<br>support@example.com
    <div class="social-row"><span></span><span></span><span></span><span></span></div>
  </div>
  <div class="copy">Copyright @ 2016 . All Rights Reserved.</div>
</footer>

</body>
</html>
```